Amber Hollow Productions

I need a business card design for a new freelance film production company using or incorporating the logo:
I want the card to be creative, minimal, yet professional. Feel free to use a variety of different shapes and sizes/ textures for the card.

Industry/Entity Type

Film Production

```html
<!DOCTYPE html>
<html lang="en">
<head>
<meta charset="utf-8">
<title>Amber Hollow Productions – Business Card</title>
<link rel="stylesheet" href="https://fonts.googleapis.com/css2?family=Exo+2:wght@400;500&display=swap">
<style>
  :root {
    --backdrop: #2b2b2b;
    --card-light: #ffffff;
    --card-shade: #cfcfcf;
    --brand-blue: #2c4585;
    --ink: #1e1e1e;
  }
  html, body {
    margin: 0;
    padding: 0;
    width: 1200px;
    height: 751px;
    overflow: hidden;
    background: var(--backdrop);
  }
  .canvas {
    position: relative;
    width: 1200px;
    height: 751px;
    font-family: "Exo 2", "Helvetica Neue", Arial, sans-serif;
  }
  .card-shapes {
    position: absolute;
    inset: 0;
  }
  .card-front-face,
  .card-back-face {
    position: absolute;
    display: flex;
    flex-direction: column;
    align-items: center;
    justify-content: center;
    text-align: center;
  }
  .card-front-face {
    left: 178px;
    top: 180px;
    width: 375px;
    height: 200px;
  }
  .brand-name {
    margin: 0;
    color: var(--brand-blue);
    font-weight: 500;
    font-size: 30px;
    line-height: 1.2;
    letter-spacing: 0.5px;
  }
  .card-back-face {
    left: 611px;
    top: 362px;
    width: 376px;
    height: 90px;
    color: var(--ink);
    font-weight: 400;
  }
  .contact-phone {
    font-size: 19px;
    margin: 0 0 6px;
    letter-spacing: 0.3px;
  }
  .contact-line {
    font-size: 15.5px;
    margin: 0 0 6px;
    letter-spacing: 0.3px;
  }
</style>
</head>
<body>
<div class="canvas">
  <svg class="card-shapes" width="1200" height="751" viewBox="0 0 1200 751" aria-hidden="true">
    <defs>
      <linearGradient id="card-sheen" x1="0" y1="0" x2="1" y2="0">
        <stop offset="0" stop-color="var(--card-light)"/>
        <stop offset="1" stop-color="var(--card-shade)"/>
      </linearGradient>
    </defs>
    <!-- front card: film strip with sprocket holes -->
    <path class="film-strip-card" fill="url(#card-sheen)" fill-rule="evenodd"
      d="M200,127 h331 a22,22 0 0 1 22,22 v269 a22,22 0 0 1 -22,22 h-331 a22,22 0 0 1 -22,-22 v-269 a22,22 0 0 1 22,-22 z
         M202,137h37v36h-37z M260,137h37v36h-37z M318,137h37v36h-37z M376,137h37v36h-37z M434,137h37v36h-37z M492,137h37v36h-37z
         M202,386h37v36h-37z M260,386h37v36h-37z M318,386h37v36h-37z M376,386h37v36h-37z M434,386h37v36h-37z M492,386h37v36h-37z"/>
    <!-- back card: film strip with sprocket holes -->
    <path class="film-strip-card" fill="url(#card-sheen)" fill-rule="evenodd"
      d="M633,262 h332 a22,22 0 0 1 22,22 v266 a22,22 0 0 1 -22,22 h-332 a22,22 0 0 1 -22,-22 v-266 a22,22 0 0 1 22,-22 z
         M635,273h37v36h-37z M692,273h37v36h-37z M750,273h37v36h-37z M808,273h37v36h-37z M866,273h37v36h-37z M923,273h37v36h-37z
         M635,519h37v36h-37z M692,519h37v36h-37z M750,519h37v36h-37z M808,519h37v36h-37z M866,519h37v36h-37z M923,519h37v36h-37z"/>
  </svg>

  <section class="card-front-face">
    <h1 class="brand-name">Amber Hollow<br>Productions</h1>
  </section>

  <section class="card-back-face">
    <p class="contact-phone">318.555.04127</p>
    <p class="contact-line">mara.quill@amberhollow.com</p>
    <p class="contact-line">Cedar Falls, Ohio</p>
  </section>
</div>
</body>
</html>
```